Post Lockdown Ortho Special

We are running a special for (Ortho) Braces/Clear Aligner (Quorvelina), till July 31st 2020. Up to $2,000 off with free Consultation and Xrays.

We need a ad to run in different formats.

Maybe something with: what better time to get braces when you have to wear a mask all the time.

Trying to rebuild our business and get people in for free consultations.

```html
<!DOCTYPE html>
<html lang="en">
<head>
<meta charset="utf-8">
<title>Post Lockdown Ortho Special</title>
<link rel="stylesheet" href="https://fonts.googleapis.com/css2?family=Montserrat:wght@400;500;700&family=Oswald:wght@500;600&display=swap">
<style>
  :root {
    --page: #dcdcdc;
    --paper: #f4f4f5;
    --purple: #6a48a2;
    --purple-light: #7b5eae;
    --headline: #6a44a6;
    --ink: #222226;
    --blush: #f7dfe3;
    --ring: #e9d8e6;
    --white: #ffffff;
    --muted: #7a6f86;
  }
  * { box-sizing: border-box; margin: 0; padding: 0; }
  html, body { width: 1200px; height: 2666px; overflow: hidden; }
  body { background: var(--page); font-family: "Montserrat", Arial, sans-serif; position: relative; }

  .flyer {
    position: absolute; left: 98px; top: 1167px;
    width: 1000px; height: 1287px;
    background: var(--paper); overflow: hidden;
  }
  .photo { position: absolute; }
  .photo--smile-hero {
    left: 574px; top: 0; width: 426px; height: 638px;
    background: radial-gradient(ellipse at 60% 55%, #f2cfc3 0%, #e8b8ad 45%, #f3ece9 80%, #f6f4f4 100%);
  }
  .headline { position: absolute; left: 76px; top: 78px; width: 520px; }
  .headline__intro { font-size: 47px; font-weight: 400; line-height: 51px; color: var(--ink); }
  .headline__offer { font-size: 70px; font-weight: 700; line-height: 71px; color: var(--headline); margin-top: 4px; }

  .band { position: absolute; left: 0; top: 638px; width: 1000px; height: 429px; }
  .band svg { display: block; }

  .thumb {
    position: absolute; width: 223px; height: 223px; border-radius: 50%;
    border: 12px solid var(--ring); box-shadow: 0 10px 18px rgba(60,30,90,0.25);
  }
  .thumb--aligner { left: 78px; top: 508px; background: radial-gradient(circle, #f1d3cc 0%, #d89d97 60%, #e9c0b5 100%); }
  .thumb--braces { left: 321px; top: 508px; background: radial-gradient(circle, #f3ddd6 0%, #d39b93 55%, #ecc8bd 100%); }

  .pitch-bar { position: absolute; left: 78px; top: 781px; width: 6px; height: 145px; background: var(--white); }
  .pitch {
    position: absolute; left: 117px; top: 784px;
    font-size: 28px; line-height: 37px; color: var(--white); white-space: nowrap;
  }
  .pitch strong { color: var(--blush); font-weight: 700; }
  .divider { position: absolute; left: 496px; top: 781px; width: 6px; height: 145px; background: var(--white); }

  .deal { position: absolute; left: 567px; top: 706px; color: var(--white); }
  .deal__upto { font-size: 36px; line-height: 40px; }
  .deal__amount { display: flex; align-items: center; margin-top: 0; height: 116px; }
  .deal__price { font-family: "Oswald", "Arial Narrow", sans-serif; font-weight: 600; font-size: 112px; line-height: 116px; color: var(--blush); letter-spacing: -3px; }
  .deal__off {
    position: absolute; left: 302px; top: 52px; width: 47px; height: 95px; background: var(--blush);
    display: flex; align-items: center; justify-content: center;
  }
  .deal__off span { transform: rotate(-90deg); font-weight: 700; font-size: 26px; color: var(--purple); letter-spacing: 1px; }
  .deal__extra { font-size: 40px; line-height: 40px; margin-top: 14px; }
  .deal__date { position: absolute; left: 705px; top: 1014px; font-size: 18px; color: var(--white); }

  .photo--dentist {
    left: 0; top: 925px; width: 497px; height: 362px;
    background: linear-gradient(160deg, #e9eef5 0%, #b9c9dd 45%, #6d86b0 75%, #3b2f2b 100%);
    clip-path: polygon(42% 0, 72% 0, 100% 45%, 100% 100%, 0 100%, 0 40%, 20% 28%);
  }

  .brand { position: absolute; left: 543px; top: 1118px; display: flex; align-items: center; }
  .brand__mark { width: 100px; height: 100px; border-radius: 50%; background: var(--purple-light); }
  .brand__text { margin-left: 37px; }
  .brand__name { font-size: 36px; line-height: 38px; font-weight: 700; color: var(--purple); }
  .brand__name small { display: block; font-size: 14px; line-height: 20px; letter-spacing: 6px; font-weight: 700; }
  .brand__doctor { font-size: 14px; letter-spacing: 1px; color: var(--muted); margin-top: 4px; padding-left: 20px; }
</style>
</head>
<body>
  <main class="flyer">
    <div class="photo photo--smile-hero" role="img" aria-label="Close-up of a smiling woman wearing braces"></div>

    <div class="band">
      <svg width="1000" height="429" viewBox="0 0 1000 429">
        <rect width="1000" height="429" fill="var(--purple)"/>
        <path d="M 330 300 C 540 200 760 120 1000 50 L 1000 429 L 330 429 Z" fill="var(--purple-light)"/>
      </svg>
    </div>

    <div class="headline">
      <p class="headline__intro">We are running<br>a special for</p>
      <h1 class="headline__offer">(Ortho)<br>Braces/Clear<br>Aligner<br>(Quorvelina)</h1>
    </div>

    <div class="thumb thumb--aligner" role="img" aria-label="Smile with a clear aligner being fitted"></div>
    <div class="thumb thumb--braces" role="img" aria-label="Smile with metal braces"></div>

    <div class="pitch-bar"></div>
    <p class="pitch">Better time to get<br>braces when you have<br>to wear a <strong>MASK</strong> all<br>the time.</p>
    <div class="divider"></div>

    <div class="deal">
      <p class="deal__upto">UPTO</p>
      <div class="deal__amount">
        <span class="deal__price">$2,000</span>
      </div>
      <span class="deal__off"><span>OFF</span></span>
      <p class="deal__extra">WITH FREE<br>CONSULTATION<br>AND XRAYS</p>
    </div>
    <p class="deal__date">TILL JULY 31ST 2020</p>

    <div class="photo photo--dentist" role="img" aria-label="Dentist in face shield and mask examining a patient in the chair"></div>

    <div class="brand">
      <div class="brand__mark"></div>
      <div class="brand__text">
        <p class="brand__name">PINECREST<small>FAMILY DENTISTRY</small></p>
        <p class="brand__doctor">DR MARLENE ASHBY</p>
      </div>
    </div>
  </main>
</body>
</html>
```